VelloCap Nutrition Require Label Design Assistance

We are VelloCap!

We are a new mushroom focused nutrition supplement company looking for some design assistance. We are looking to provide some of the highest quality mushroom supplements available on the market today, using 100% fruiting bodies where many other companies opt for cheaper alternatives. We strongly believe in the power of mushroom nutrition and wish to focus on the high-end supplement market.

We are starting with three initial ranges; Lions Mane, Turkey Tail and Reishi - and wish to have powerful yet elegant designs for each. We wish to be visually appealing whilst maintaining the high-end feel. Imagery of the mushrooms on the label would be good if it maintains high-end appeal. Our bottles will be dark green and lids will be white if this helps with visualization. We have a logo and preferred font for the name which can be used if possible. The image in the logo may need resizing to fit with the supplement market (smaller logo/larger font). If you provide a superior logo to that which we currently have, we would consider using it.

The three range designs should be the same, but with the mushroom name and any imagery changed to reflect the different ranges. I am happy to supply images where required.

Label dimensions = 55mm x 150mm

Target Market(s)

Premium High End Health Supplements

Industry/Entity Type

Supplement

Font styles to use
Serif
Sans Serif

Colors

Designer to choose colors to be used in the design.

Requirements
Must have
• Must have the text "100% Fruiting Bodies"
• Must have Organic + Vegan notification.
• Must have an ingredients section, and there will need to be some space for small-print (which will be decided on shortly).
Nice to have
• See label specifications in message thread.

```html
<!DOCTYPE html>
<html lang="en">
<head>
<meta charset="utf-8">
<title>VelloCap Mushroom Capsule Labels</title>
<link rel="stylesheet" href="https://fonts.googleapis.com/css2?family=Playfair+Display:wght@800&family=Questrial&family=Josefin+Sans:wght@400&display=swap">
<style>
  :root {
    --backdrop: #737373;
    --label-paper: #ffffff;
    --halo: #f6f6f6;
    --gold: #a8862a;
    --ink: #1f1f1f;
    --turkey-moss: #5c8a2c;
    --turkey-tan: #d2ae76;
    --lions-forest: #2e3a31;
    --lions-white: #dfe9e6;
    --reishi-red: #8e3226;
    --reishi-brown: #3c1b13;
  }
  html, body {
    margin: 0;
    padding: 0;
    overflow: hidden;
  }
  .canvas {
    position: relative;
    width: 1200px;
    height: 848px;
    background: var(--backdrop);
    overflow: hidden;
  }
  .label {
    position: absolute;
    top: 179px;
    width: 340px;
    height: 403px;
    background: var(--label-paper);
  }
  .label--turkey { left: 46px; }
  .label--lions { left: 423px; }
  .label--reishi { left: 804px; }
  .label svg { display: block; width: 100%; height: 100%; overflow: hidden; }
  .brand-name {
    font-family: 'Josefin Sans', sans-serif;
    font-size: 22px;
    letter-spacing: 3px;
    fill: var(--ink);
  }
  .cap-halo { fill: var(--halo); }
  .arc-claim {
    font-family: 'Questrial', sans-serif;
    font-size: 30px;
    fill: var(--ink);
  }
  .range-name {
    font-family: 'Playfair Display', serif;
    font-weight: 800;
    font-size: 74px;
    fill: var(--gold);
    text-anchor: middle;
  }
  .badge-line {
    font-family: 'Questrial', sans-serif;
    font-size: 38px;
    fill: var(--ink);
    text-anchor: middle;
  }
  .badge-plus { font-size: 30px; }
  .count-number {
    font-family: 'Questrial', sans-serif;
    font-size: 104px;
    fill: var(--gold);
    text-anchor: middle;
  }
  .count-unit {
    font-family: 'Questrial', sans-serif;
    font-size: 34px;
    fill: var(--ink);
    text-anchor: middle;
  }
  .ingredient {
    font-family: 'Questrial', sans-serif;
    font-size: 25px;
    fill: var(--ink);
  }
</style>
</head>
<body>
<div class="canvas">

  <!-- Turkey Tail -->
  <section class="label label--turkey">
    <svg viewBox="0 0 650 769">
      <defs>
        <linearGradient id="turkey-tone" x1="0" y1="0" x2="1" y2="1">
          <stop offset="0" stop-color="var(--turkey-moss)"/>
          <stop offset="0.5" stop-color="var(--turkey-tan)"/>
          <stop offset="1" stop-color="var(--turkey-moss)"/>
        </linearGradient>
        <path id="arc-turkey" d="M374,86 Q548,118 610,320"/>
      </defs>
      <text class="brand-name" x="27" y="124">VelloCap</text>
      <path class="cap-halo" d="M55,300 C80,180 200,85 350,83 C490,82 590,180 600,285 C605,330 570,335 540,325 C460,300 400,292 330,294 C230,296 150,318 95,333 C60,340 50,325 55,300 Z"/>
      <path role="img" aria-label="Photo of turkey tail mushroom on moss" fill="url(#turkey-tone)" d="M76,303 C110,200 220,105 350,102 C470,100 560,200 580,288 C584,304 574,310 558,305 C470,280 400,270 330,272 C230,275 150,295 95,308 C80,312 72,310 76,303 Z"/>
      <text class="arc-claim"><textPath href="#arc-turkey" textLength="300" lengthAdjust="spacingAndGlyphs">% 100 Fruiting Bodies</textPath></text>
      <text class="range-name" x="327" y="358" textLength="157" lengthAdjust="spacingAndGlyphs">TURKEY</text>
      <text class="range-name" x="327" y="421" textLength="105" lengthAdjust="spacingAndGlyphs">TAIL</text>
      <text class="badge-line" x="325" y="460">Organic</text>
      <text class="badge-line badge-plus" x="325" y="482">+</text>
      <text class="badge-line" x="325" y="507">Vegan</text>
      <text class="count-number" x="325" y="590">60</text>
      <text class="count-unit" x="325" y="619">capsules</text>
      <text class="ingredient" x="75" y="685" textLength="394" lengthAdjust="spacingAndGlyphs">Turkey Tail Organic Fruiting Bodies</text>
      <text class="ingredient" x="490" y="685" textLength="79" lengthAdjust="spacingAndGlyphs">600mg</text>
      <text class="ingredient" x="75" y="715" textLength="240" lengthAdjust="spacingAndGlyphs">Organic Enoki Extract</text>
      <text class="ingredient" x="505" y="715" textLength="64" lengthAdjust="spacingAndGlyphs">25mg</text>
      <text class="ingredient" x="75" y="745" textLength="106" lengthAdjust="spacingAndGlyphs">Curcumin</text>
      <text class="ingredient" x="492" y="745" textLength="77" lengthAdjust="spacingAndGlyphs">100mg</text>
    </svg>
  </section>

  <!-- Lions Mane -->
  <section class="label label--lions">
    <svg viewBox="0 0 650 769">
      <defs>
        <linearGradient id="lions-tone" x1="0" y1="0" x2="1" y2="0">
          <stop offset="0" stop-color="var(--lions-forest)"/>
          <stop offset="0.3" stop-color="var(--lions-white)"/>
          <stop offset="0.75" stop-color="var(--lions-white)"/>
          <stop offset="1" stop-color="var(--lions-forest)"/>
        </linearGradient>
        <path id="arc-lions" d="M374,86 Q548,118 610,320"/>
      </defs>
      <text class="brand-name" x="29" y="124">VelloCap</text>
      <path class="cap-halo" d="M55,300 C80,180 200,85 350,83 C490,82 590,180 600,285 C605,330 570,335 540,325 C460,300 400,292 330,294 C230,296 150,318 95,333 C60,340 50,325 55,300 Z"/>
      <path role="img" aria-label="Photo of lion's mane mushroom in forest" fill="url(#lions-tone)" d="M76,303 C110,200 220,105 350,102 C470,100 560,200 580,288 C584,304 574,310 558,305 C470,280 400,270 330,272 C230,275 150,295 95,308 C80,312 72,310 76,303 Z"/>
      <text class="arc-claim"><textPath href="#arc-lions" textLength="300" lengthAdjust="spacingAndGlyphs">% 100 Fruiting Bodies</textPath></text>
      <text class="range-name" x="327" y="358" textLength="130" lengthAdjust="spacingAndGlyphs">LIONS</text>
      <text class="range-name" x="327" y="421" textLength="134" lengthAdjust="spacingAndGlyphs">MANE</text>
      <text class="badge-line" x="327" y="460">Organic</text>
      <text class="badge-line badge-plus" x="327" y="482">+</text>
      <text class="badge-line" x="327" y="507">Vegan</text>
      <text class="count-number" x="327" y="590">60</text>
      <text class="count-unit" x="327" y="619">capsules</text>
      <text class="ingredient" x="80" y="709" textLength="405" lengthAdjust="spacingAndGlyphs">Lions Mane Organic Fruiting Bodies</text>
      <text class="ingredient" x="494" y="709" textLength="81" lengthAdjust="spacingAndGlyphs">700mg</text>
      <text class="ingredient" x="80" y="739" textLength="145" lengthAdjust="spacingAndGlyphs">Ginko Bilbao</text>
      <text class="ingredient" x="511" y="739" textLength="64" lengthAdjust="spacingAndGlyphs">35mg</text>
    </svg>
  </section>

  <!-- Reishi -->
  <section class="label label--reishi">
    <svg viewBox="0 0 650 769">
      <defs>
        <linearGradient id="reishi-tone" x1="0" y1="0" x2="1" y2="1">
          <stop offset="0" stop-color="var(--reishi-red)"/>
          <stop offset="0.55" stop-color="var(--reishi-red)"/>
          <stop offset="1" stop-color="var(--reishi-brown)"/>
        </linearGradient>
        <path id="arc-reishi" d="M374,90 Q548,124 610,326"/>
      </defs>
      <text class="brand-name" x="24" y="124">VelloCap</text>
      <path class="cap-halo" d="M55,305 C80,185 200,90 350,88 C490,87 590,185 600,290 C605,335 570,340 540,330 C460,305 400,297 330,299 C230,301 150,323 95,338 C60,345 50,330 55,305 Z"/>
      <path role="img" aria-label="Photo of reishi mushroom caps" fill="url(#reishi-tone)" d="M76,310 C110,205 220,110 350,108 C470,106 560,205 580,293 C584,309 574,315 558,310 C470,285 400,275 330,277 C230,280 150,300 95,313 C80,317 72,315 76,310 Z"/>
      <text class="arc-claim"><textPath href="#arc-reishi" textLength="300" lengthAdjust="spacingAndGlyphs">% 100 Fruiting Bodies</textPath></text>
      <text class="range-name" x="329" y="410" textLength="140" lengthAdjust="spacingAndGlyphs">REISHI</text>
      <text class="badge-line" x="327" y="460">Organic</text>
      <text class="badge-line badge-plus" x="327" y="482">+</text>
      <text class="badge-line" x="327" y="507">Vegan</text>
      <text class="count-number" x="327" y="590">60</text>
      <text class="count-unit" x="327" y="619">capsules</text>
      <text class="ingredient" x="107" y="709" textLength="340" lengthAdjust="spacingAndGlyphs">Reishi Organic Fruiting Bodies</text>
      <text class="ingredient" x="467" y="709" textLength="80" lengthAdjust="spacingAndGlyphs">700mg</text>
      <text class="ingredient" x="107" y="739" textLength="214" lengthAdjust="spacingAndGlyphs">Green Tea Powder</text>
      <text class="ingredient" x="480" y="739" textLength="64" lengthAdjust="spacingAndGlyphs">35mg</text>
    </svg>
  </section>

</div>
</body>
</html>
```